Business Card for Managing Partner Investment Fund

To create a business card template for an investment fund manager. Business card should be more professional in nature, not too colorful, more upscale, and created using the attached logos and fund name files. I would prefer a black or gray color scheme, but am open to the use of color as well. I would prefer a double sided business card, but open to single sided business card designs as well. The business card should include: name, title, and contact information, as well as logo and company name. I would prefer a more stream-lined, simple business card design.
Updates
Address: 4190 NE 38th Ter. Ocala, FL 34470
Email: talvin47@quorimail.net
Phone: 561-347-9162
Title: managing partner
Name: Dorian Velsky
Fund Name: Ambergate Capital
Logos can be found in files attached to the brief
Target Market(s)
potential investors, other fund managers
Industry/Entity Type
Finance
Contact Information for Business Card
Name on card: Dorian Velsky
Title: Managing Partner
Colors
Designer to choose colors to be used in the design.
Requirements
Must have
- Phone number
- email address
- physical address
- title
- name
- logo
- Fund name
Nice to have
- simple layout
Should not have
- too many colors, busy fonts,

```html
<!DOCTYPE html>
<html lang="en">
<head>
<meta charset="utf-8">
<title>Ambergate Capital – Business Card</title>
<link rel="stylesheet" href="https://fonts.googleapis.com/css2?family=Libre+Caslon+Text:wght@700&family=PT+Sans:wght@400&display=swap">
<style>
  :root {
    --backdrop: #e8e5e1;
    --card-black: #050505;
    --text-white: #ffffff;
    --silver-light: #f2f2f2;
    --silver-mid: #cfcfcf;
    --silver-dark: #a9a9a9;
    --mark-ink: #1a1a1a;
  }
  * { margin: 0; padding: 0; box-sizing: border-box; }
  html, body {
    width: 1200px;
    height: 900px;
    overflow: hidden;
    background: var(--backdrop);
  }
  .canvas {
    position: relative;
    width: 1200px;
    height: 900px;
  }
  .card {
    position: absolute;
    left: 120px;
    top: 155px;
    width: 960px;
    height: 591px;
    background: var(--card-black);
    border-radius: 26px;
    overflow: hidden;
    color: var(--text-white);
  }
  .holder-name {
    position: absolute;
    left: 52px;
    top: 70px;
    font-family: "Libre Caslon Text", "Times New Roman", serif;
    font-weight: 700;
    font-size: 36px;
    letter-spacing: 0.5px;
    text-transform: uppercase;
    line-height: 1;
  }
  .holder-title {
    position: absolute;
    left: 52px;
    top: 118px;
    font-family: "PT Sans", Arial, sans-serif;
    font-size: 24px;
    line-height: 1;
  }
  .contact-list {
    position: absolute;
    left: 50px;
    top: 364px;
    font-family: "PT Sans", Arial, sans-serif;
    font-size: 25px;
    line-height: 1;
    list-style: none;
  }
  .contact-item {
    display: flex;
    align-items: center;
    gap: 8px;
    height: 35px;
  }
  .contact-icon {
    width: 22px;
    height: 22px;
    fill: var(--text-white);
    flex: none;
  }
  .contact-address {
    margin-top: 14px;
    line-height: 35px;
    padding-left: 2px;
  }
  .brand-disc {
    position: absolute;
    left: 377px;
    top: 41px;
    width: 508px;
    height: 508px;
    border-radius: 50%;
    background: radial-gradient(circle at 40% 35%, var(--silver-light) 0%, var(--silver-mid) 60%, var(--silver-dark) 100%);
  }
  .brand-name {
    position: absolute;
    left: 377px;
    top: 238px;
    width: 508px;
    text-align: center;
    font-family: "Libre Caslon Text", "Times New Roman", serif;
    font-weight: 700;
    font-size: 52px;
    letter-spacing: 4px;
    line-height: 66px;
    text-transform: uppercase;
    color: var(--mark-ink);
  }
</style>
</head>
<body>
<main class="canvas">
  <section class="card">
    <h1 class="holder-name">Dorian Velsky</h1>
    <p class="holder-title">Managing Partner</p>

    <ul class="contact-list">
      <li class="contact-item">
        <svg class="contact-icon" viewBox="0 0 24 24" aria-hidden="true">
          <path d="M6.6 10.8c1.4 2.8 3.8 5.1 6.6 6.6l2.2-2.2c.3-.3.7-.4 1-.2 1.1.4 2.3.6 3.6.6.6 0 1 .4 1 1V20c0 .6-.4 1-1 1C10.6 21 3 13.4 3 4c0-.6.4-1 1-1h3.5c.6 0 1 .4 1 1 0 1.3.2 2.5.6 3.6.1.3 0 .7-.2 1z"/>
        </svg>
        <span>561-347-9162</span>
      </li>
      <li class="contact-item">
        <svg class="contact-icon" viewBox="0 0 24 24" aria-hidden="true">
          <path d="M3 6h18v12H3z M3 6l9 7 9-7" fill="none" stroke="#ffffff" stroke-width="0"/>
          <path d="M3 5h18a1 1 0 0 1 1 1v.4l-10 7-10-7V6a1 1 0 0 1 1-1zM2 8.8l10 7 10-7V18a1 1 0 0 1-1 1H3a1 1 0 0 1-1-1z"/>
        </svg>
        <span>talvin47@quorimail.net</span>
      </li>
      <li class="contact-address">4190 NE 38th Ter.<br>Ocala, FL 34470</li>
    </ul>

    <div class="brand-disc" role="img" aria-label="Brushed silver disc with faint mountain landscape behind the fund name"></div>
    <p class="brand-name">Ambergate<br>Capital</p>
  </section>
</main>
</body>
</html>
```